Business Card Design for Engineering Firm

Need a business card design for small mechanical and plumbing engineering form based in Utah. Design should be customizable for all employees.

```html
<!DOCTYPE html>
<html lang="en">
<head>
<meta charset="utf-8">
<title>Bramwell Engineering – Business Card</title>
<link href="https://fonts.googleapis.com/css2?family=Lato:wght@400;700;900&display=swap" rel="stylesheet">
<style>
  :root {
    --backdrop: #1d1d1f;
    --card-white: #ffffff;
    --card-grey: #545456;
    --brand-red: #7d0000;
    --ink-grey: #4a4a4a;
  }
  * { margin: 0; padding: 0; box-sizing: border-box; }
  html, body {
    width: 1200px; height: 801px; overflow: hidden;
    background: var(--backdrop);
    font-family: "Lato", Arial, sans-serif;
  }
  .stage { position: relative; width: 1200px; height: 801px; }
  .card {
    position: absolute; top: 246px;
    width: 540px; height: 309px;
    overflow: hidden;
    box-shadow: 0 14px 30px rgba(0,0,0,.55);
  }
  .card--front { left: 52px; background: var(--card-white); }
  .card--back { left: 608px; background: var(--card-grey); }

  .front-band { position: absolute; inset: 0; }

  .person { position: absolute; left: 34px; top: 52px; }
  .person__name {
    font-weight: 900; font-size: 25px; letter-spacing: .5px;
    color: var(--brand-red); text-transform: uppercase; line-height: 1;
  }
  .person__role {
    font-size: 15px; color: var(--ink-grey); margin-top: 4px; letter-spacing: .3px;
  }
  .contact { position: absolute; left: 34px; top: 124px; list-style: none; }
  .contact__item {
    display: flex; align-items: flex-start; gap: 10px;
    font-size: 12.5px; color: var(--ink-grey); line-height: 17px;
    margin-bottom: 3px; letter-spacing: .3px;
  }
  .contact__icon { width: 12px; height: 12px; margin-top: 2px; flex: none; fill: var(--brand-red); }

  .brand {
    position: absolute; inset: 0;
    display: flex; align-items: center; justify-content: center; gap: 14px;
  }
  .brand__mark { width: 30px; height: 30px; background: var(--brand-red); }
  .brand__name {
    font-weight: 900; font-size: 30px; letter-spacing: 1px;
    color: var(--brand-red); text-transform: uppercase;
  }
</style>
</head>
<body>
<main class="stage">

  <section class="card card--front" aria-label="Card front">
    <svg class="front-band" viewBox="0 0 540 309" aria-hidden="true">
      <polygon points="440,0 540,0 540,309 438,309 540,150" fill="var(--brand-red)"/>
    </svg>

    <div class="person">
      <h1 class="person__name">Daniel Harlow</h1>
      <p class="person__role">Founder &amp; CEO</p>
    </div>

    <ul class="contact">
      <li class="contact__item">
        <svg class="contact__icon" viewBox="0 0 12 12"><path d="M6 0a4 4 0 0 0-4 4c0 3 4 8 4 8s4-5 4-8a4 4 0 0 0-4-4zm0 5.5A1.5 1.5 0 1 1 6 2.5a1.5 1.5 0 0 1 0 3z"/></svg>
        <span>482 Granite Ave.<br>Sandy, UT 84070</span>
      </li>
      <li class="contact__item">
        <svg class="contact__icon" viewBox="0 0 12 12"><path d="M2.5 0 4.5 2.5 3.3 4a7 7 0 0 0 4.7 4.7L9.5 7.5 12 9.5 10.5 12C5 12 0 7 0 1.5z"/></svg>
        <span>(801) 555-0142</span>
      </li>
      <li class="contact__item">
        <svg class="contact__icon" viewBox="0 0 12 12"><path d="M3 0h6a1 1 0 0 1 1 1v10a1 1 0 0 1-1 1H3a1 1 0 0 1-1-1V1a1 1 0 0 1 1-1zm0 1.5v8h6v-8z"/></svg>
        <span>(801) 555-0187</span>
      </li>
      <li class="contact__item">
        <svg class="contact__icon" viewBox="0 0 12 12"><path d="M3 0h6v3H3zM1 4h10a1 1 0 0 1 1 1v4h-2v3H2V9H0V5a1 1 0 0 1 1-1zm2 4v3h6V8z"/></svg>
        <span>(801) 555-0199</span>
      </li>
      <li class="contact__item">
        <svg class="contact__icon" viewBox="0 0 12 12"><path d="M0 2h12v1L6 7 0 3zm0 2.3 6 4 6-4V10H0z"/></svg>
        <span>info@bramwelleng.com</span>
      </li>
      <li class="contact__item">
        <svg class="contact__icon" viewBox="0 0 12 12"><path d="M6 0a6 6 0 1 0 0 12A6 6 0 0 0 6 0zm0 1.3c.8 0 1.6 1.8 1.8 4H4.2C4.4 3.1 5.2 1.3 6 1.3zM4.2 6.7h3.6c-.2 2.2-1 4-1.8 4s-1.6-1.8-1.8-4z"/></svg>
        <span>www.bramwelleng.com</span>
      </li>
    </ul>
  </section>

  <section class="card card--back" aria-label="Card back">
    <div class="brand">
      <span class="brand__mark" aria-hidden="true"></span>
      <span class="brand__name">Bramwell Engineering</span>
    </div>
  </section>

</main>
</body>
</html>
```